business card design for a small scale specialty cut flower farm

We need a business card design for Hollowmere Bloom Farm based in Langley, BC, Canada. We produce specialty, high-end cut flowers and sell locally to florists, local shops and markets and the end user through bouquet subscriptions. The final business card design should be memorable and have a timeless or vintage feel. We would prefer a square shape.
Updates

Target Market(s)

florists, shops and seasonal markets, local flower lovers

Industry/Entity Type

Floral

Contact Information for Business Card

Tamsin Ellery Voss, Grower
Langley, BC, Canada
website: hollowmerebloomfarm.example
instagram: @hollowmerebloomfarm
Tel: 555.317.4290
facebook: www.facebook.example/hollowmereblooms/

Font styles to use
Serif
Decorative
Script

Requirements
Must have
• soft black background colour on front side, the included logo and catch phrase: Fresh Local Seasonal
Nice to have
• phone number and website address on front of card, included photo 6539 incorporated onto the back, possibly photo 6609 as well.

```html
<!DOCTYPE html>
<html lang="en">
<head>
<meta charset="utf-8">
<title>Hollowmere Bloom Farm – Business Card</title>
<link href="https://fonts.googleapis.com/css2?family=Mulish:wght@300;400;500&display=swap" rel="stylesheet">
<style>
  :root {
    --backdrop: #8c8d8c;
    --card-light: #ffffff;
    --card-dark: #231f20;
    --ink: #231f20;
    --ink-soft: #8a8a8a;
    --paper-text: #ffffff;
    --bloom-deep: #3a3033;
    --bloom-mid: #2c2628;
  }
  * { box-sizing: border-box; margin: 0; padding: 0; }
  html, body { width: 1200px; height: 960px; overflow: hidden; }
  body {
    background: var(--backdrop);
    font-family: "Mulish", sans-serif;
    position: relative;
  }
  .card {
    position: absolute;
    top: 150px;
    width: 377px;
    height: 663px;
    border-radius: 28px;
    overflow: hidden;
  }
  .card--contact { left: 206px; background: var(--card-light); }
  .card--brand { left: 600px; background: var(--card-dark); }

  .brand-mark {
    position: absolute;
    left: 0; right: 0;
    display: flex;
    flex-direction: column;
    align-items: center;
    gap: 14px;
  }
  .brand-mark__dot {
    width: 58px; height: 58px;
    border-radius: 50%;
    background: #e9a9c6;
  }
  .brand-mark__name {
    font-weight: 400;
    font-size: 17px;
    letter-spacing: 4px;
    text-transform: uppercase;
    text-align: center;
    line-height: 1.5;
  }
  .card--contact .brand-mark { top: 62px; }
  .card--contact .brand-mark__name { color: var(--ink); }
  .card--brand .brand-mark { top: 330px; }
  .card--brand .brand-mark__name { color: var(--paper-text); font-size: 20px; }

  .accent-bar {
    position: absolute;
    left: 0; top: 436px;
    width: 10px; height: 177px;
    background: var(--ink);
  }
  .person {
    position: absolute;
    left: 57px; top: 436px;
  }
  .person__name { font-size: 24px; font-weight: 500; color: var(--ink); line-height: 1.2; }
  .person__role { font-size: 17px; font-weight: 300; color: var(--ink-soft); margin-top: 2px; }

  .contact-list {
    position: absolute;
    left: 57px; top: 514px;
    list-style: none;
  }
  .contact-list li {
    display: flex; align-items: center; gap: 9px;
    height: 24px;
    font-size: 16px; font-weight: 300; color: var(--ink-soft);
  }
  .contact-list svg, .contact-list .icon-dot {
    width: 17px; height: 17px; flex: none;
  }
  .icon-dot { border-radius: 50%; background: var(--ink); }

  .bloom-photo {
    position: absolute;
    left: 0; top: 0;
    width: 100%; height: 270px;
    background: radial-gradient(ellipse 60% 70% at 50% 35%, var(--bloom-deep) 0%, var(--bloom-mid) 60%, var(--card-dark) 100%);
  }
  .catchphrase {
    position: absolute;
    left: 24px; right: 24px; top: 582px;
    display: flex; align-items: center; gap: 8px;
    color: var(--paper-text);
    font-size: 17px; font-weight: 400;
    white-space: nowrap;
  }
  .catchphrase::before, .catchphrase::after {
    content: ""; flex: 1; height: 1px; background: var(--paper-text);
  }
</style>
</head>
<body>
  <section class="card card--contact">
    <div class="brand-mark">
      <span class="brand-mark__dot"></span>
      <span class="brand-mark__name">Hollowmere<br>Bloom Farm</span>
    </div>
    <span class="accent-bar"></span>
    <div class="person">
      <p class="person__name">Tamsin Ellery Voss</p>
      <p class="person__role">Owner</p>
    </div>
    <ul class="contact-list">
      <li>
        <svg viewBox="0 0 20 20" aria-hidden="true"><circle cx="10" cy="10" r="10" fill="#231f20"/><path d="M7 5l2 2-1 1.5a6 6 0 0 0 3.5 3.5L13 11l2 2-1.5 1.5C9.5 14 6 10.5 5.5 6.5z" fill="#fff"/></svg>
        (555) 317-4290
      </li>
      <li>
        <svg viewBox="0 0 20 20" aria-hidden="true"><circle cx="10" cy="10" r="10" fill="#231f20"/><g fill="none" stroke="#fff" stroke-width="1.1"><circle cx="10" cy="10" r="6"/><ellipse cx="10" cy="10" rx="2.6" ry="6"/><path d="M4 10h12M5 7h10M5 13h10"/></g></svg>
        hollowmerebloomfarm.example
      </li>
      <li><span class="icon-dot"></span>@hollowmerebloomfarm</li>
      <li><span class="icon-dot"></span>hollowmereblooms</li>
    </ul>
  </section>

  <section class="card card--brand">
    <div class="bloom-photo" role="img" aria-label="Faint close-up photograph of a wild rose bloom"></div>
    <div class="brand-mark">
      <span class="brand-mark__dot"></span>
      <span class="brand-mark__name">Hollowmere<br>Bloom Farm</span>
    </div>
    <p class="catchphrase">Fresh Local Seasonal</p>
  </section>
</body>
</html>
```